Single Page Production Company Site

Clean. Simple. Minimalist site with one page.

No portfolio, just some text to communicate a general overview of what the company does.

We work for a very select group of clients, creating strong brand personalities online. The site is specifically minimal and not communicating too much about what we do.. we have a variety of capabilities to work with clients and prefer to be broad with just a simple landing page as the point of contact for our brand.
Updates

Christmas holidays are coming up, maybe people need some time away from work with family and friends... We can keep working on this and I will provide feedback as quickly as possible, but I understand if designers have other commitments during the coming days. Thanks for your hard work!

Industry/Entity Type

Design Agency

Coding

Coded - Design and coding required

Number of Pages Required

1 page

Font styles to use
Sans Serif

Requirements
Must have
• Clean, bold text headlines.
Nice to have
• Unsure about any images used in the design, would like to see options with or without.

```html
<!DOCTYPE html>
<html lang="en">
<head>
<meta charset="utf-8">
<title>Design Agency</title>
<link rel="stylesheet" href="https://fonts.googleapis.com/css2?family=League+Spartan:wght@700;800;900&family=Josefin+Sans:wght@400;600&family=Ubuntu:wght@400;500&family=Lato:wght@300;400&display=swap">
<style>
:root{
  --yellow:#f5eb6a;
  --ink:#111111;
  --grey:#e6e6e6;
  --body:#444444;
  --muted:#777777;
  --line:#9a9a9a;
  --footer:#000000;
  --footer-text:#8a8a8a;
}
*{box-sizing:border-box;margin:0;padding:0}
html,body{width:1200px;height:3169px;overflow:hidden;background:#fff}
.page{position:relative;width:1200px;height:3169px;overflow:hidden;font-family:'Lato',sans-serif;color:var(--ink)}
.abs{position:absolute}

.hero{left:0;top:0;width:1200px;height:662px;background:var(--yellow)}
.brand{left:54px;top:46px;font-family:'Ubuntu',sans-serif;font-weight:500;font-size:40px;letter-spacing:-1px}
.menu{left:1063px;top:47px;width:48px;height:40px}
.hero-title{left:0;top:246px;width:1278px;text-align:center;font-family:'League Spartan',sans-serif;font-weight:900;font-size:88px;letter-spacing:1px;line-height:1}
.hero-copy{left:0;top:356px;width:1200px;text-align:center;font-family:'Josefin Sans',sans-serif;font-weight:600;font-size:15px;line-height:20px;letter-spacing:-.3px}
.hero-btn{left:505px;top:427px;width:178px;height:60px;border:3px solid var(--ink);font-family:'Ubuntu',sans-serif;font-size:28px;line-height:54px;text-align:center}

.feature{width:320px;text-align:center}
.feature-icon{display:block;margin:0 auto;width:64px;height:64px;background:var(--yellow)}
.feature-title{margin-top:40px;font-family:'Josefin Sans',sans-serif;font-weight:600;font-size:21px;letter-spacing:-.5px}
.feature-text{margin:16px auto 0;width:280px;font-family:'Josefin Sans',sans-serif;font-size:11px;line-height:16px;color:var(--muted)}

.about{left:0;top:1044px;width:1200px;height:1477px;background:var(--grey)}
.stripe{top:1044px;width:161px;height:1477px;background:var(--yellow)}
.block-title{font-family:'Ubuntu',sans-serif;font-size:29px;color:var(--ink);line-height:1}
.block-text{font-family:'Lato',sans-serif;font-weight:300;font-size:17px;line-height:24.6px;color:var(--body)}
.right{text-align:right}

.contact-title{left:0;top:2566px;width:1200px;text-align:center;font-family:'Ubuntu',sans-serif;font-size:29px;letter-spacing:1px}
.field{left:382px;width:430px;height:44px;border:2px solid var(--line);font-family:'Lato',sans-serif;font-weight:300;font-size:12px;color:#b5b5b5;padding:18px 0 0 18px}
.send{left:549px;top:2927px;width:137px;height:44px;background:var(--yellow);font-family:'League Spartan',sans-serif;font-weight:800;font-size:19px;line-height:48px;text-align:center}

.footer{left:0;top:3052px;width:1200px;height:117px;background:var(--footer)}
.social{left:56px;top:3079px;display:flex;gap:26px}
.social span{font-family:'Lato',sans-serif;font-weight:400;font-size:18px;color:#fff;line-height:28px}
.copyright{right:42px;top:3084px;font-family:'Lato',sans-serif;font-weight:300;font-size:15px;color:var(--footer-text)}
</style>
</head>
<body>
<div class="page">

  <header class="abs hero"></header>
  <div class="abs brand">LOGO</div>
  <svg class="abs menu" viewBox="0 0 48 40" aria-label="Menu">
    <rect x="0" y="0" width="48" height="9" rx="4.5" fill="#111"/>
    <rect x="0" y="15.5" width="48" height="9" rx="4.5" fill="#111"/>
    <rect x="0" y="31" width="48" height="9" rx="4.5" fill="#111"/>
  </svg>
  <h1 class="abs hero-title">DESIGN&nbsp;&nbsp;AGENCY</h1>
  <p class="abs hero-copy">We work for a very select group of clients&nbsp; creating strong brand personalities online.<br>The site is speci&nbsp; cally minimal and not communicating too much about what we do.. .</p>
  <div class="abs hero-btn">More info</div>

  <section class="abs feature" style="left:73px;top:756px">
    <svg class="feature-icon" viewBox="0 0 64 64" aria-label="Idea icon">
      <rect width="64" height="64" fill="#f5eb6a"/>
      <path d="M32 14a13 13 0 0 0-8 23v6h16v-6a13 13 0 0 0-8-23z" fill="none" stroke="#111" stroke-width="2"/>
      <path d="M26 47h12M28 51h8" stroke="#111" stroke-width="2"/>
      <circle cx="32" cy="27" r="4" fill="none" stroke="#111" stroke-width="2"/>
    </svg>
    <h3 class="feature-title" style="margin-top:38px">DESIGN HAPPENS HERE</h3>
    <p class="feature-text">We are leading the way in design innovation for modern websites. Clean functional intuitive websites for progressive businesses.</p>
  </section>

  <section class="abs feature" style="left:443px;top:756px">
    <svg class="feature-icon" viewBox="0 0 64 64" aria-label="Edit icon">
      <rect width="64" height="64" fill="#f5eb6a"/>
      <path d="M34 18H16v30h30V30" fill="none" stroke="#111" stroke-width="2.5"/>
      <path d="M28 36l2-7 16-16 5 5-16 16z" fill="none" stroke="#111" stroke-width="2.5"/>
    </svg>
    <h3 class="feature-title">ART HAPPENS HERE</h3>
    <p class="feature-text">Building brands through design&nbsp; we believe that contrast is everything. For industry leaders who set the pace and exceed expectations&nbsp; we help give the company voice and soul.</p>
  </section>

  <section class="abs feature" style="left:785px;top:756px">
    <svg class="feature-icon" viewBox="0 0 64 64" aria-label="Tick icon">
      <rect width="64" height="64" fill="#f5eb6a"/>
      <rect x="16" y="16" width="32" height="32" rx="3" fill="none" stroke="#111" stroke-width="3" stroke-dasharray="5 3"/>
      <path d="M22 31l8 8 16-20" fill="none" stroke="#111" stroke-width="5"/>
    </svg>
    <h3 class="feature-title">IDEAS HAPPEN HERE</h3>
    <p class="feature-text">Clients look to us for unique&nbsp; exceptional solutions to their technology issues. We bring creativity to the table and solve your business&nbsp; problems with actionable solutions.</p>
  </section>

  <section class="abs about"></section>
  <div class="abs stripe" style="left:158px"></div>
  <div class="abs stripe" style="left:833px"></div>

  <h2 class="abs block-title" style="left:79px;top:1095px">The Harbor Team</h2>
  <p class="abs block-text" style="left:78px;top:1136px">Harbor Row Studio focuses on creating<br>extraordinary online experiences for extraordinary<br>clients. We'll work with<br>you to create the perfect online presence<br>for your brand.</p>

  <h2 class="abs block-title right" style="right:76px;top:1327px">Size is Everything</h2>
  <p class="abs block-text right" style="right:72px;top:1379px">We don't work in a massive corporate office and we don't<br>have a mailroom. Not that there's anything wrong with that<br>, it's just that we like knowing each other's names, and<br>encourage our clients to know ours. Our small staf has an<br>advantage our group works more ciently, more cost-efectively<br>and most importantly, exible to each client's unique needs.<br>We deliver a range of services found at any agency<br>, with the personal service you should expect.</p>

  <h2 class="abs block-title" style="left:85px;top:1636px">Our Goal</h2>
  <p class="abs block-text" style="left:78px;top:1691px">Harbor Row brings your brand to life, online.<br>We do it all when it comes to online commerce for<br>retail stores,wholesalers and distributors. Taking your<br>company online introduces a world of opportunity, as<br>well as specif challenges associated with online trade.<br>We'll assist you in establishing a successful online<br>presence and bringing your brand to a worldwide<br>audience.</p>

  <h2 class="abs block-title right" style="right:72px;top:1939px">whos reed?</h2>
  <p class="abs block-text right" style="right:72px;top:1991px">Harbor Row brings your brand to life, online<br>We do it all when it comes to online commerce for<br>retail stores,wholesalers and distributors. Taking your<br>company online introduces a world of opportunity, as<br>well as specif challenges associated with online trade<br>We'll assist you in establishing a successful online<br>presence and bringing your brand to a worldwide<br>audience.</p>

  <h2 class="abs block-title" style="left:86px;top:2229px">We get you</h2>
  <p class="abs block-text" style="left:81px;top:2287px">Having a website isn't enough. You need to show your customers<br>you understand the socially connected online world we live in.<br>We help you create designs that capture the personality of your<br>business and project the image you want your customers to see.<br>Maybe you're a small company looking to sell yourself in the big<br>leagues; maybe you're a big company that wants to look<br>approachable; either way, we can make it happen.</p>

  <h2 class="abs contact-title">CONTACT&nbsp; FORM</h2>
  <div class="abs field" style="top:2630px">your name is here</div>
  <div class="abs field" style="top:2698px;left:384px">Email</div>
  <div class="abs field" style="top:2762px;left:383px">phone</div>
  <div class="abs field" style="top:2820px;left:383px;height:70px">Message</div>
  <div class="abs send">LOGIN</div>

  <footer class="abs footer"></footer>
  <nav class="abs social">
    <span>Follow</span><span>Chat</span><span>Watch</span><span>Feed</span>
  </nav>
  <p class="abs copyright">© 2016 Marlow. All rights reserved by hello@harborrowstudio.com</p>

</div>
</body>
</html>
```